Label for packaging - front and back

Hello,
We are looking for a fresh design based off of the current one we have. We need something fresh simple and eye catching. Company is MeadowGlint.com I am including current packaging and also a trim fold fliers we had made.
MG Brochure is what we could use as design inspiration perhaps?
Updates
PLEASE replace super food with " Beyond Super Food". somewhere on the label. In addition, please include website name on front.
Target Market(s)
Nutrition, athletes, anyone who wants to improve health
Look and feel
Each slider illustrates characteristics of the customer's brand and the style your logo design should communicate.

```html
<!DOCTYPE html>
<html lang="en">
<head>
<meta charset="utf-8">
<title>MeadowGlint Spirulina Label</title>
<link rel="stylesheet" href="https://fonts.googleapis.com/css2?family=Source+Sans+3:ital,wght@0,400;0,600;0,700;1,400;1,600;1,700;1,800&display=swap">
<style>
  :root {
    --backdrop: #353333;
    --white: #ffffff;
    --band-grey: #a6a6a8;
    --teal: #16a394;
    --teal-dark: #0f8d80;
    --ink: #444446;
    --navy: #14234a;
    --note-grey: #707072;
    --meadow-pale: #eef3dc;
    --meadow: #c6e27a;
    --meadow-deep: #8fc43e;
    --powder: #2f7a5e;
  }
  * { margin: 0; padding: 0; box-sizing: border-box; }
  html, body {
    width: 1200px; height: 1200px; overflow: hidden;
    background: var(--backdrop);
    font-family: "Source Sans 3", sans-serif;
  }
  .label {
    position: absolute; left: 284px; top: 148px;
    width: 632px; height: 904px;
    border-radius: 20px; overflow: hidden;
    background: var(--white);
  }
  .header { position: absolute; left: 0; top: 0; width: 632px; height: 164px; }
  .header svg { display: block; }
  .brand-name {
    position: absolute; left: 12px; top: 118px; width: 130px;
    text-align: center;
    font-weight: 600; font-size: 21px; color: var(--navy);
    letter-spacing: 0.5px;
  }
  .product-title {
    position: absolute; left: 240px; top: 2px;
    font-weight: 700; font-style: italic; font-size: 84px;
    color: var(--white); line-height: 1;
  }
  .product-species {
    position: absolute; left: 310px; top: 83px;
    font-weight: 700; font-style: italic; font-size: 24px;
    letter-spacing: 17px; color: var(--white); line-height: 1;
  }
  .tagline {
    position: absolute; left: 263px; top: 124px;
    font-weight: 600; font-style: italic; font-size: 22.5px;
    color: var(--white); line-height: 1;
  }
  .hero {
    position: absolute; left: 0; top: 164px; width: 632px; height: 651px;
    background:
      radial-gradient(circle at 80% 18%, rgba(160,205,90,0.5), rgba(160,205,90,0) 45%),
      radial-gradient(ellipse at 20% 95%, rgba(110,185,50,0.6), rgba(110,185,50,0) 55%),
      linear-gradient(180deg, var(--meadow-pale) 0%, #e3efbf 30%, var(--meadow) 65%, var(--meadow-deep) 100%);
  }
  .powder-bowl {
    position: absolute; left: 258px; top: 177px; width: 370px; height: 370px;
    border-radius: 50%;
    background: radial-gradient(circle, var(--powder) 0, var(--powder) 156px, #d9ddd6 158px, #ffffff 166px, #f4f6ef 175px, rgba(244,247,236,0) 185px);
  }
  .claim {
    position: absolute; left: 42px; top: 100px;
    font-weight: 700; font-style: italic; font-size: 57px;
    color: var(--teal); line-height: 1; white-space: nowrap;
  }
  .benefits { position: absolute; left: 24px; top: 190px; list-style: none; }
  .benefit {
    display: flex; align-items: center; height: 40px; margin-bottom: 10px;
    font-weight: 700; font-style: italic; font-size: 31px; color: var(--ink);
  }
  .benefit-icon {
    width: 40px; height: 40px; border-radius: 50%;
    background: radial-gradient(circle at 35% 30%, #34c0ae, var(--teal-dark));
    margin-right: 13px; flex: none;
    display: flex; align-items: center; justify-content: center;
  }
  .website {
    position: absolute; left: 24px; top: 604px;
    font-weight: 700; font-style: italic; font-size: 22px;
    color: var(--white); line-height: 1;
  }
  .footer { position: absolute; left: 0; top: 815px; width: 632px; height: 89px; }
  .footer svg { position: absolute; left: 0; top: 0; }
  .stat {
    position: absolute; top: 46px;
    font-weight: 700; font-style: italic; font-size: 20px;
    color: var(--white); line-height: 1;
  }
  .stat-divider { position: absolute; top: 35px; width: 1.5px; height: 35px; background: var(--white); }
  .net-weight {
    position: absolute; left: 500px; top: 18px; width: 90px;
    text-align: center; font-style: italic; font-size: 16px;
    color: var(--note-grey); line-height: 1.4;
  }
</style>
</head>
<body>
<main class="label">
  <header class="header">
    <svg width="632" height="164" viewBox="0 0 632 164" aria-hidden="true">
      <defs>
        <linearGradient id="moss" x1="0" y1="0" x2="1" y2="1">
          <stop offset="0" stop-color="#2b8b5b"/>
          <stop offset="0.5" stop-color="#1d7249"/>
          <stop offset="1" stop-color="#2f9262"/>
        </linearGradient>
      </defs>
      <rect x="0" y="0" width="632" height="124" fill="url(#moss)"/>
      <path d="M0,11 H126 C160,11 170,60 190,90 C205,110 225,114 260,114 H632 V164 H0 Z" fill="#ffffff"/>
      <path d="M185,100 C205,125 225,155 270,155 H632 V122 H255 C225,122 205,118 185,100 Z" fill="#a6a6a8"/>
    </svg>
    <div class="brand-name">MeadowGlint</div>
    <h1 class="product-title">Spirulina</h1>
    <div class="product-species">PLATENSIS</div>
    <p class="tagline">Freeze dried to preserve all nutrition</p>
  </header>

  <section class="hero">
    <div class="powder-bowl" role="img" aria-label="White bowl filled with green spirulina powder among soft fresh leaves"></div>
    <h2 class="claim">Beyond Super Food</h2>
    <ul class="benefits">
      <li class="benefit">
        <span class="benefit-icon">
          <svg width="22" height="22" viewBox="0 0 22 22" fill="none" stroke="#fff" stroke-width="1.4" aria-hidden="true">
            <path d="M11,9 C8,6 5,8 7,10 L11,13 L15,10 C17,8 14,6 11,9 Z"/>
            <path d="M3,13 C6,14 9,17 11,19 C13,17 16,14 19,13"/>
          </svg>
        </span>Chlorophyll
      </li>
      <li class="benefit">
        <span class="benefit-icon">
          <svg width="22" height="22" viewBox="0 0 22 22" fill="none" stroke="#fff" stroke-width="1.4" aria-hidden="true">
            <rect x="3" y="11" width="16" height="7" rx="3.5"/>
            <line x1="11" y1="11" x2="11" y2="18"/>
            <path d="M11,9 C11,6 12,4 14,3 M11,8 C10,6 9,5 8,5"/>
          </svg>
        </span>Antioxidants
      </li>
      <li class="benefit">
        <span class="benefit-icon">
          <svg width="22" height="22" viewBox="0 0 22 22" fill="none" stroke="#fff" stroke-width="1.4" aria-hidden="true">
            <rect x="3" y="11" width="16" height="7" rx="3.5"/>
            <line x1="11" y1="11" x2="11" y2="18"/>
            <path d="M11,9 C11,6 12,4 14,3 M11,8 C10,6 9,5 8,5"/>
          </svg>
        </span>Vitamins
      </li>
    </ul>
    <p class="website">MeadowGlint.com</p>
  </section>

  <footer class="footer">
    <svg width="632" height="89" viewBox="0 0 632 89" aria-hidden="true">
      <defs>
        <linearGradient id="mossFoot" x1="0" y1="0" x2="1" y2="0">
          <stop offset="0" stop-color="#1f7a4f"/>
          <stop offset="0.5" stop-color="#2c8c5d"/>
          <stop offset="1" stop-color="#1b6f48"/>
        </linearGradient>
      </defs>
      <rect x="0" y="0" width="632" height="16" fill="#ffffff"/>
      <rect x="0" y="16" width="632" height="73" fill="url(#mossFoot)"/>
      <path d="M420,16 C455,16 470,33 485,51 C495,63 505,67 525,67 H632 V16 Z" fill="#ffffff"/>
    </svg>
    <span class="stat" style="left:23px">PROTEIN 70%</span>
    <span class="stat-divider" style="left:169px"></span>
    <span class="stat" style="left:189px">AMINO ACIDS</span>
    <span class="stat-divider" style="left:334px"></span>
    <span class="stat" style="left:352px">VITAMINS</span>
    <div class="net-weight">Net weight<br>120g</div>
  </footer>
</main>
</body>
</html>
```